都内でエステサロンを運営されている
美容家さんの電子書籍を出版しますので、
表紙デザイン作成をお願いいたします。

ーーーーーーーーーーー
■本のタイトル
月灯集

【サブタイトル】
朝の散歩で心を整える本

<著者>沙耶(さや)

ーーーーーーーーーー

納品は、2,560 x 1,600 ピクセルのJPEGと
元データをお願い致したく。

著者プロフィール
美容家、エステティシャン

サロンのイメージカラーはピンク、白ですが
表紙デザインに色のこだわりはありません。

ーーーー

■デザイン要望

優しさ,明るさ、清潔感と品格、プロフェッショナル感があるものをお願いします。

【コンセプト】
美容ジプシー、悩める女性たちに(男性も歓迎)贈りたい
優しく楽しい小さなご褒美タイムとその作法(洗顔やお肌のお手入れに関するメソッド)を提供する

肌質はみんなそれぞれちがいますが、本当に幸せな自分磨きは毎日のスキンケア一択。その極意を惜しみなく提供。

添付に表紙イメージの参考を挙げましたが
デザイナー様のセンスにお任せします。

ーーーーーーーーーー

※その他イラストや写真等素材を使用される場合には、商用利用可の素材をお願いします。
(Pavrelにて販売予定のため)

デザインを考えるのに必要な情報などありましたら、お答えしますので、ご遠慮なくお問い合わせ下さい。

納期は予告なく短縮する場合がございます。
よろしくお願い申し上げます。

著者様のご希望優先で決定させていただきました。

美容の道を極めた想いと、透明感、躍動感、生き生きとした理想の美人像を彷彿とさせる素敵な表紙ということで、選定させていただきます。

この度は、当コンペにご提案を頂き誠にありがとうございます。
リピートのデザイナー様もいらして、どれも素晴らしく貴重なお時間と労力を割いてくださって
本当にありがとうございました。心より感謝申し上げます。

今回選定できなかった方々の作品も大切に拝見し、個別に依頼できそうな案件などありましたらご紹介させていただきます。みなさまのご活躍祈念しております。

これからも大切に作品を制作してまいります。
どうぞまたコンペ開催の際にはご縁をいただけましたら幸いです。

本当にどうもありがとうございました。

```html
<!DOCTYPE html>
<html lang="ja">
<head>
<meta charset="utf-8">
<title>月灯集 表紙</title>
<link rel="stylesheet" href="https://fonts.googleapis.com/css2?family=Shippori+Mincho+B1:wght@500;700;800&family=M+PLUS+Rounded+1c:wght@800&family=Cormorant+Garamond:wght@500&display=swap">
<style>
  :root {
    --paper: #fffafb;
    --glow: #fde6ec;
    --pink: #e7869d;
    --pink-deep: #dc5f7f;
    --rose-light: #f7d3dc;
    --rose-mid: #f0b3c1;
    --ink: #2f2a2c;
    --label: #c9a3ad;
  }
  * { margin: 0; padding: 0; box-sizing: border-box; }
  html, body { width: 750px; height: 1200px; overflow: hidden; background: var(--paper); }
  .cover {
    position: relative;
    width: 750px;
    height: 1200px;
    overflow: hidden;
    background: radial-gradient(ellipse 70% 40% at 50% 22%, var(--glow) 0%, var(--paper) 70%);
  }
  .cover-art {
    position: absolute;
    left: 0; top: 560px;
    width: 750px; height: 640px;
    background:
      radial-gradient(ellipse 40% 45% at 50% 45%, #fbe3e6 0%, transparent 70%),
      linear-gradient(180deg, rgba(247,211,220,0) 0%, var(--rose-light) 28%, var(--rose-mid) 100%);
  }
  .romaji {
    position: absolute;
    top: 78px; width: 100%;
    text-align: center;
    font-family: "Cormorant Garamond", serif;
    font-weight: 500;
    font-size: 40px;
    letter-spacing: 6px;
    color: var(--label);
  }
  .title {
    position: absolute;
    top: 122px; width: 100%;
    text-align: center;
    font-family: "Shippori Mincho B1", serif;
    font-weight: 700;
    font-size: 150px;
    line-height: 1;
    letter-spacing: 8px;
    color: var(--pink);
  }
  .subtitle {
    position: absolute;
    top: 318px; width: 100%;
    text-align: center;
    font-family: "M PLUS Rounded 1c", sans-serif;
    font-weight: 800;
    font-size: 42px;
    line-height: 1.45;
    color: var(--pink);
  }
  .subtitle .accent { color: var(--pink-deep); }
  .author {
    position: absolute;
    top: 510px; left: 150px;
    font-family: "Shippori Mincho B1", serif;
    font-weight: 700;
    color: var(--ink);
    display: flex;
    align-items: flex-end;
    gap: 14px;
  }
  .author .role { font-size: 27px; }
  .author .name { font-size: 42px; line-height: 1; }
  .author rt { font-size: 16px; font-weight: 500; }
  .author .mark { font-size: 27px; }
  .tagline {
    position: absolute;
    top: 495px; right: 26px;
    writing-mode: vertical-rl;
    font-family: "Shippori Mincho B1", serif;
    font-weight: 800;
    font-size: 46px;
    line-height: 1.2;
    color: var(--ink);
    text-shadow: 0 0 6px #fff, 0 0 6px #fff;
  }
  .promise {
    position: absolute;
    top: 655px; left: 28px;
    writing-mode: vertical-rl;
    font-family: "Shippori Mincho B1", serif;
    font-weight: 800;
    font-size: 44px;
    line-height: 1.15;
    color: var(--pink-deep);
    -webkit-text-stroke: 0;
    text-shadow: 0 0 3px #fff, 0 0 3px #fff, 0 0 6px #fff, 0 0 8px #fff;
  }
</style>
</head>
<body>
  <main class="cover">
    <div class="cover-art" role="img" aria-label="目を閉じて頬杖をつく長い髪の女性と、周囲に咲く淡いピンクのバラの花々のイラスト"></div>

    <p class="romaji">GETTOSHU</p>
    <h1 class="title">月灯集</h1>
    <p class="subtitle"><span class="accent">朝の散歩</span>で<br>心を整える本</p>

    <p class="author">
      <span class="role">美容家エステティシャン</span>
      <ruby class="name">沙耶<rt>さや</rt></ruby>
      <span class="mark">著</span>
    </p>

    <p class="tagline">美容ジプシー、<br>お肌に悩む人に贈る</p>

    <p class="promise">優しく楽しい<br>小さなご褒美タイムと<br>その作法</p>
  </main>
</body>
</html>
```